Telmoro Business Card

I already have the conplay logo. I need to develop a professional business card layout

Target Market(s)

Business

Industry/Entity Type

Business

Contact Information for Business Card

Company Name: Telmoro Limited

Font styles to use
Sans Serif

Colors

Designer to choose colors to be used in the design.

Requirements
Must have
• Use current logo
• Need two card size options:
• Small Card: 70mm x 28mm (Landscape)
• Square Card: 65mm x 65mm
Nice to have
• I will need 8-10 files for each name, number and email address (details to follow)

```html
<!DOCTYPE html>
<html lang="en">
<head>
<meta charset="UTF-8">
<title>Telmoro Business Card</title>
<link href="https://fonts.googleapis.com/css2?family=Roboto:wght@400;700&family=Roboto+Condensed:wght@700&display=swap" rel="stylesheet">
<style>
  :root {
    --backdrop: #2b2b2b;
    --green-light: #7cbb2a;
    --green-mid: #2f9a2f;
    --green-deep: #036b30;
    --card-white: #ffffff;
    --text-light: #ffffff;
    --brand-green: #056b2f;
  }
  html, body {
    margin: 0;
    padding: 0;
    width: 1200px;
    height: 960px;
    overflow: hidden;
    background: var(--backdrop);
  }
  .canvas {
    position: relative;
    width: 1200px;
    height: 960px;
  }
  .card {
    position: absolute;
    width: 384px;
    height: 384px;
    box-sizing: border-box;
  }
  .card--front {
    left: 249px;
    top: 294px;
    background: radial-gradient(circle at 50% 52%, var(--green-light) 0%, var(--green-mid) 38%, var(--green-deep) 72%);
    color: var(--text-light);
    font-family: "Roboto", Arial, sans-serif;
    text-align: center;
  }
  .card--back {
    left: 671px;
    top: 295px;
    background: var(--card-white);
    display: flex;
    align-items: center;
    justify-content: center;
  }
  .contact {
    position: absolute;
    left: 0;
    right: 0;
    top: 106px;
    margin: 0 auto;
    width: 384px;
    transform: translateX(-1px);
  }
  .contact__name {
    font-family: "Roboto Condensed", "Arial Narrow", sans-serif;
    font-weight: 700;
    font-size: 20px;
    letter-spacing: 0.2px;
    line-height: 26px;
    margin: 0;
  }
  .contact__divider {
    display: block;
    width: 72px;
    height: 1px;
    margin: 12px auto 11px;
    background: linear-gradient(90deg, rgba(255,255,255,0), rgba(255,255,255,0.9), rgba(255,255,255,0));
  }
  .contact__lines {
    margin: 0;
    font-size: 14.5px;
    line-height: 19px;
  }
  .contact__lines--reach {
    letter-spacing: 0.3px;
  }
  .contact__divider--second {
    margin: 10px auto 12px;
  }
  .brand-name {
    font-family: "Roboto", Arial, sans-serif;
    font-weight: 700;
    font-size: 48px;
    letter-spacing: 1px;
    color: var(--brand-green);
    transform: translate(-8px, 0);
  }
</style>
</head>
<body>
  <main class="canvas">
    <section class="card card--front" aria-label="Business card front">
      <div class="contact">
        <h1 class="contact__name">MARK ELLISON</h1>
        <span class="contact__divider"></span>
        <p class="contact__lines">4120 Cedar Hollow Road<br>Juneau, Alaska 36218</p>
        <span class="contact__divider contact__divider--second"></span>
        <p class="contact__lines contact__lines--reach">P. 612 508 3947<br>E . mark@telmoro.com<br>www.telmoro.com</p>
      </div>
    </section>
    <section class="card card--back" aria-label="Business card back">
      <span class="brand-name">TELMORO</span>
    </section>
  </main>
</body>
</html>
```